Audio Visual company needs brochure design

We are an AV company that does Audio Visual work solely for Commercial customers. We Design, sale and install various Audio Visual systems for our customers. This may be something as simple as a conference room, a new sound system for a church or a new sound, lighting and video system for an arena or stadium.

We don't really have any ideas in mind and that's the reason we are turning to you. We want something that highlights what we do, and something they will look at - not just toss in the can.

Included is a copy of our logo (sorry it's the only copy we have now)

Our company name is Velmira Staging www.velmirastaging.example
Updates

Reason: The rest of our management team hasn't provided feedback to me yet. We will pick the design this week.

Target Market(s)

70% of our business is churches and the remaining is corporate customers and restaurants.

Industry/Entity Type

Church

Requirements
Must have
• The brochure will be 8.5" x 11" printed both sides - open to Z fold or Tri fold designs. We can provide pictures of our work if needed - though they may not be the best.
Should not have
• No generic pictures of just speakers, projectors, microphones, etc.

```html
<!DOCTYPE html>
<html lang="en">
<head>
<meta charset="utf-8">
<title>Velmira Staging – Tri-fold Brochure</title>
<link rel="stylesheet" href="https://fonts.googleapis.com/css2?family=Open+Sans:wght@400;600;700&family=Oswald:wght@500&display=swap">
<style>
  :root {
    --page-bg: #e7e5e1;
    --panel-top: #ffffff;
    --panel-bottom: #dde7f2;
    --ink: #2b2b2b;
    --brand-blue: #2d3592;
    --accent-blue: #1f8fd6;
    --light-blue: #8fd0f2;
    --deep-navy: #0a1030;
    --stage-blue: #1c3fa8;
    --fold: #c3cad4;
    --logo-grey: #3a3a3a;
  }
  * { margin: 0; padding: 0; box-sizing: border-box; }
  html, body { width: 1200px; height: 982px; overflow: hidden; }
  body {
    background: var(--page-bg);
    font-family: "Open Sans", Arial, sans-serif;
    color: var(--ink);
    position: relative;
  }
  .brochure {
    position: absolute;
    left: 72px; top: 83px;
    width: 1056px; height: 816px;
    background: linear-gradient(180deg, var(--panel-top) 40%, var(--panel-bottom) 100%);
    box-shadow: 0 6px 18px rgba(0,0,0,.25);
    overflow: hidden;
  }
  .panel { position: absolute; top: 0; height: 816px; width: 352px; }
  .panel--services { left: 0; background: linear-gradient(160deg, #ffffff 35%, #d3e1f0 100%); }
  .panel--contact { left: 352px; border-left: 1px solid var(--fold); }
  .panel--cover { left: 704px; border-left: 1px solid var(--fold); }

  .art { position: absolute; left: 0; top: 0; }
  .art--arena { width: 352px; height: 360px; }
  .art--stage { left: 352px; width: 704px; height: 520px; }

  .section-title {
    position: absolute;
    font-size: 23px; font-weight: 400; color: var(--brand-blue);
    letter-spacing: -.2px;
  }
  .section-title b { font-weight: 700; }
  .section-rule {
    position: absolute; height: 2px;
    background: linear-gradient(90deg, var(--light-blue), rgba(143,208,242,.2));
  }
  .services-title { left: 18px; top: 448px; }
  .services-rule { left: 18px; top: 482px; width: 380px; }
  .services-copy {
    position: absolute; left: 18px; top: 488px; width: 320px;
    font-size: 13.6px; line-height: 20px;
  }
  .solutions-title { right: 20px; top: 640px; left: auto; }
  .solutions-rule { left: 104px; top: 674px; width: 230px;
    background: linear-gradient(270deg, var(--light-blue), rgba(143,208,242,.2)); }
  .solutions-copy {
    position: absolute; right: 20px; top: 682px; width: 310px;
    font-size: 13.6px; line-height: 20px; text-align: right;
  }
  .phone-line {
    position: absolute; display: flex; align-items: center; gap: 6px;
    font-size: 13.4px; color: var(--brand-blue);
  }
  .services-phone { right: 22px; top: 755px; }

  .quote {
    position: absolute; left: 458px; top: 42px; width: 330px;
    font-family: "Oswald", "Arial Narrow", sans-serif; font-weight: 500;
    font-size: 27px; line-height: 38px; color: #fff; text-align: center;
    text-shadow: 0 2px 4px rgba(0,0,0,.6);
  }

  .wordmark {
    position: absolute; font-weight: 700; color: var(--logo-grey);
    letter-spacing: -.5px; white-space: nowrap;
  }
  .wordmark--small { left: 26px; top: 580px; font-size: 25px; }
  .wordmark--large { left: 0; width: 352px; top: 592px; text-align: center; font-size: 36px; }

  .contact-list { position: absolute; left: 30px; top: 680px; list-style: none; }
  .contact-list li {
    display: flex; align-items: center; gap: 8px;
    font-size: 13.4px; color: var(--ink); height: 20px;
  }
  .contact-list li.gap { margin-top: 20px; }

  .tagline {
    position: absolute; left: 0; width: 352px; top: 706px;
    text-align: center; font-size: 21.5px; line-height: 29px; color: var(--brand-blue);
  }
  .icon { width: 13px; height: 13px; flex: none; }
</style>
</head>
<body>
<main class="brochure">

  <section class="panel panel--services">
    <svg class="art art--arena" viewBox="0 0 352 360">
      <defs>
        <linearGradient id="arenaTone" x1="0" y1="0" x2="0" y2="1">
          <stop offset="0" stop-color="#1a4fb8"/>
          <stop offset=".35" stop-color="#26314e"/>
          <stop offset="1" stop-color="#4b5566"/>
        </linearGradient>
        <linearGradient id="arcBlue" x1="0" y1="0" x2="1" y2="0">
          <stop offset="0" stop-color="#1b6fc7"/>
          <stop offset="1" stop-color="#4fb3e8"/>
        </linearGradient>
      </defs>
      <rect width="352" height="360" fill="url(#arenaTone)" role="img" aria-label="Photo of an arena interior with blue ceiling lights and tiered seating"/>
      <path d="M0,330 C70,292 170,282 250,296 C300,305 335,320 352,336 L352,360 L0,360 Z" fill="url(#arcBlue)"/>
      <path d="M0,342 C80,306 180,298 260,312 C305,320 335,332 352,344 L352,360 L0,360 Z" fill="#ffffff"/>
    </svg>

    <h2 class="section-title services-title"><b>Our</b>Services</h2>
    <div class="section-rule services-rule"></div>
    <p class="services-copy">We Design, sale and install various Audio Visual systems for our customers. This may be something as simple as a conference room, a new sound system for a church or a new sound, lighting and video system for an arena or stadium.</p>

    <h2 class="section-title solutions-title"><b>Smart</b>Solutions</h2>
    <div class="section-rule solutions-rule"></div>
    <p class="solutions-copy">Our Mission is to provide our customers with creative and unique installation and production services within budget and on time.</p>

    <p class="phone-line services-phone">
      <svg class="icon" viewBox="0 0 16 16"><circle cx="8" cy="8" r="7" fill="none" stroke="currentColor" stroke-width="1.4"/><path d="M5.5 4.5l1.5 1.5-1 1.2c.6 1.2 1.6 2.2 2.8 2.8l1.2-1 1.5 1.5-1 1.2C8 11.4 5 8.4 4.3 5.5z" fill="currentColor"/></svg>
      555 - 014 - 2287
    </p>
  </section>

  <svg class="art art--stage" viewBox="0 0 704 520">
    <defs>
      <linearGradient id="stageTone" x1="0" y1="0" x2="0" y2="1">
        <stop offset="0" stop-color="#0c1a5e"/>
        <stop offset=".45" stop-color="#2a57c8"/>
        <stop offset=".8" stop-color="#121a3a"/>
        <stop offset="1" stop-color="#05070f"/>
      </linearGradient>
      <linearGradient id="swoosh" x1="0" y1="0" x2="1" y2="0">
        <stop offset="0" stop-color="#1e2f8c"/>
        <stop offset=".6" stop-color="#2c8fd8"/>
        <stop offset="1" stop-color="#6cc6f0"/>
      </linearGradient>
      <linearGradient id="panelFill" x1="0" y1="0" x2="0" y2="1">
        <stop offset="0" stop-color="#ffffff"/>
        <stop offset="1" stop-color="#f2f6fb"/>
      </linearGradient>
    </defs>
    <rect width="704" height="470" fill="url(#stageTone)" role="img" aria-label="Photo of a worship band performing on a stage lit with blue lights and truss towers"/>
    <path d="M0,420 C150,470 320,480 470,430 C580,395 650,360 704,320 L704,520 L0,520 Z" fill="#05070f"/>
    <path d="M0,470 C170,520 340,520 500,468 C590,440 660,400 704,365 L704,380 C650,420 590,455 500,482 C340,530 170,525 0,482 Z" fill="url(#swoosh)"/>
    <path d="M0,438 C160,492 330,498 490,446 C580,417 650,382 704,340 L704,350 C650,392 580,427 490,458 C330,508 160,500 0,446 Z" fill="#ffffff" opacity=".85"/>
    <path d="M0,488 C180,530 360,528 520,478 C600,452 665,414 704,384 L704,520 L0,520 Z" fill="url(#panelFill)"/>
    <line x1="352" y1="470" x2="352" y2="520" stroke="#c3cad4" stroke-width="1"/>
  </svg>

  <p class="quote">“Claraty of Message<br>through<br>clarity of sound”</p>

  <section class="panel panel--contact">
    <p class="wordmark wordmark--small">Velmira Staging</p>
    <ul class="contact-list">
      <li>
        <svg class="icon" viewBox="0 0 16 16"><circle cx="8" cy="8" r="7" fill="none" stroke="currentColor" stroke-width="1.4"/><path d="M5.5 4.5l1.5 1.5-1 1.2c.6 1.2 1.6 2.2 2.8 2.8l1.2-1 1.5 1.5-1 1.2C8 11.4 5 8.4 4.3 5.5z" fill="currentColor"/></svg>
        555 - 014 - 2287
      </li>
      <li class="gap">
        <svg class="icon" viewBox="0 0 16 16"><rect x="1.5" y="3.5" width="13" height="9" fill="none" stroke="currentColor" stroke-width="1.4"/><path d="M1.5 3.5L8 9l6.5-5.5" fill="none" stroke="currentColor" stroke-width="1.4"/></svg>
        sales@velmirastaging.example
      </li>
      <li>
        <svg class="icon" viewBox="0 0 16 16"><circle cx="8" cy="8" r="6.5" fill="none" stroke="currentColor" stroke-width="1.3"/><ellipse cx="8" cy="8" rx="3" ry="6.5" fill="none" stroke="currentColor" stroke-width="1.1"/><path d="M1.5 8h13" stroke="currentColor" stroke-width="1.1"/></svg>
        www.velmirastaging.example
      </li>
    </ul>
  </section>

  <section class="panel panel--cover">
    <p class="wordmark wordmark--large">Velmira Staging</p>
    <p class="tagline">Innovation, Motivation,<br>Satisfaction</p>
  </section>

</main>
</body>
</html>
```